Branding Guide and Website for Q7Systems

Need an experienced Graphics Designer with a proven track record to create a design and branding guide for all media formats. From this guide you will then create a new website design for Q7systems.com.
There will be 8 pages (to start) with the new website. Each page will have multiple features and panels each need to have individual attention and customization that collectively fit together into a single cohesive look and feel.
We have not been able to get good designs I’m attaching one version which is the best we’ve received which is not bad but needs to be polished up better and the images need to change. I’d like to have some other accent colors but not too much I like the white, dark blue, gray, dark gray style.
Here are some sites that I like –
http://www.brevant.com/
https://www.morvexia.com/ (layout good, graphics not great)
http://www.talsork.com/ (good layout and graphics, too much animation)
https://www.quendrapo.com/ (a little boring but the colors and some of the top images are good)
https://www.pibrostel.com/ (a little over the top colors are off but they have some good info graphics)
We don’t expect you will code the site however if you have that capability we’ll need it responsive/flat for mobile. Otherwise we can find someone to do the programming and we’ll just need the design files and images.
Branding guide will be used for web, email, print etc. so you’ll need to consider all guidelines for all formats. That is about it let me know if any questions we can have a call to discuss further if it is easier.
Not sure why they want a minimum of 300 words I’m done now but apparently have to keep typing so that is what I’m doing and Ok I’m at 300 words, almost there and we’re here now.

Target Market(s)

Customers looking for IT Services, Private Cloud, Security Services, Advanced Support, Fully Managed or Co-Managed IT.

Industry/Entity Type

It Company

Number of Pages Required

5+ page

Font styles to use
Sans Serif

Colors
0255a3
959595
e6e6e6
ffffff

Requirements
Must have
• Clean, professional and modern look using iconography, info graphics, flat etc.

```html
<!DOCTYPE html>
<html lang="en">
<head>
<meta charset="utf-8">
<title>Q7Systems – IT Service Excellence</title>
<link rel="stylesheet" href="https://fonts.googleapis.com/css2?family=Open+Sans:wght@400;600;700&family=Roboto+Condensed:wght@400;700&display=swap">
<style>
:root{
  --blue:#0255a3;
  --blue-dark:#063a73;
  --navy:#0a1e45;
  --gray:#959595;
  --gray-dark:#555;
  --light:#e6e6e6;
  --soft:#f3f3f3;
  --white:#ffffff;
  --orange:#f5a01a;
  --footer:#2a2c2e;
  --footer-text:#a9abad;
  --text:#333;
}
*{box-sizing:border-box;margin:0;padding:0}
html,body{width:1200px;height:2704px;overflow:hidden}
body{font-family:"Open Sans",Arial,sans-serif;color:var(--text);background:var(--white);position:relative}
.heading{font-family:"Roboto Condensed","Arial Narrow",sans-serif;font-weight:700;text-transform:uppercase;color:#222;text-align:center;letter-spacing:.5px}
.lead{font-size:13px;line-height:21px;color:var(--gray-dark);text-align:center}
.lead b{color:var(--blue)}

/* Header */
.site-header{position:absolute;top:0;left:0;width:1200px;height:64px;background:var(--white);display:flex;align-items:center;justify-content:space-between;padding:0 40px;border-bottom:1px solid var(--light)}
.brand{display:flex;align-items:center;gap:8px;font-weight:700;font-size:22px;color:var(--blue)}
.brand-mark{width:14px;height:14px;border-radius:50%;background:var(--blue)}
.main-nav{display:flex;gap:34px;align-items:center}
.main-nav a{font-size:11px;font-weight:600;color:var(--gray-dark);text-decoration:none;text-transform:uppercase;letter-spacing:.5px;padding:22px 0}
.main-nav a.active{color:var(--blue);border-bottom:2px solid var(--blue)}

/* Hero */
.hero{position:absolute;top:64px;left:0;width:1200px;height:456px;background:radial-gradient(ellipse at 50% 40%,#2d7fd0 0%,#0f4c9a 35%,#06265a 70%,#031636 100%);text-align:center;color:var(--white)}
.hero-title{position:absolute;top:186px;width:100%;font-family:"Roboto Condensed",sans-serif;font-weight:700;font-size:38px;letter-spacing:1px}
.hero-sub{position:absolute;top:234px;width:100%;font-size:16px;font-style:italic;font-weight:600}
.btn{display:inline-block;font-family:"Open Sans",sans-serif;font-size:11px;font-weight:700;text-transform:uppercase;letter-spacing:.5px;padding:12px 26px;text-decoration:none}
.btn-orange{background:var(--orange);color:var(--white)}
.btn-blue{background:var(--blue);color:var(--white)}
.hero .btn{position:absolute;top:282px;left:528px}
.hero-arrow{position:absolute;top:210px}
.hero-arrow.prev{left:16px}.hero-arrow.next{right:16px}

/* Services */
.services{position:absolute;top:520px;left:0;width:1200px;height:560px;background:var(--white)}
.services .heading{margin-top:70px;font-size:26px}
.services .lead{width:460px;margin:14px auto 0}
.service-grid{position:absolute;top:200px;left:110px;width:1000px;display:grid;grid-template-columns:repeat(3,1fr);row-gap:60px;column-gap:40px}
.service{display:flex;gap:16px}
.service svg{flex:0 0 40px}
.service h3{font-size:16px;font-weight:600;color:#222;margin-bottom:6px}
.service p{font-size:11px;line-height:17px;color:var(--gray)}
.divider{position:absolute;top:1080px;left:0;width:1200px;height:3px;background:var(--orange)}

/* Help */
.help{position:absolute;top:1083px;left:0;width:1200px;height:520px}
.help .heading{margin-top:38px;font-size:24px}
.help .lead{width:720px;margin:14px auto 0}
.solution-row{position:absolute;top:158px;left:120px;width:960px;display:grid;grid-template-columns:repeat(4,1fr);gap:30px;text-align:center}
.solution-photo{height:150px;border-radius:2px}
.photo-network{background:linear-gradient(135deg,#0c2b5c,#2e6fc0)}
.photo-web{background:linear-gradient(135deg,#1d5fa8,#7fb4e6)}
.photo-apps{background:linear-gradient(135deg,#3e6a94,#c9d7e4)}
.photo-mind{background:linear-gradient(135deg,#b7c3cf,#eef1f4)}
.solution h3{font-size:17px;font-weight:600;color:#222;margin-top:16px}
.solution p{font-size:11px;line-height:16px;color:var(--gray);margin-top:6px;padding:0 14px}
.partner-note{position:absolute;top:410px;width:100%;font-size:11px;color:var(--gray);text-align:center}
.partner-note b{color:var(--blue)}
.partners{position:absolute;top:448px;left:160px;width:880px;display:flex;justify-content:space-between;align-items:center}
.partner{display:flex;align-items:center;gap:7px;font-size:19px;font-weight:600;color:#8a8a8a}
.partner i{width:16px;height:16px;background:#8a8a8a;display:block}
.partner i.round{border-radius:50%}

/* Testimonials */
.testimonials{position:absolute;top:1608px;left:0;width:1200px;height:270px;background:var(--soft)}
.testimonials .heading{margin-top:44px;font-size:24px}
.quote-row{position:absolute;top:112px;left:110px;width:980px;display:grid;grid-template-columns:repeat(3,1fr);gap:50px;text-align:center}
.quote p{font-size:11px;line-height:17px;font-style:italic;color:var(--gray-dark)}
.quote cite{display:block;margin-top:14px;font-size:11px;font-style:italic;font-weight:700;color:var(--blue)}

/* Difference */
.difference{position:absolute;top:1878px;left:0;width:1200px;height:410px;background:linear-gradient(90deg,var(--white) 60%,#eef2f6 100%)}
.difference .heading{position:absolute;top:52px;left:300px;width:600px;font-size:24px}
.difference .lead{position:absolute;top:96px;left:300px;width:600px}
.difference .btn{position:absolute;top:222px;left:530px}
.difference-art{position:absolute;top:30px;left:960px;width:190px;height:300px;border-radius:4px;background:linear-gradient(180deg,#e4ebf2,#c6d3e0)}

/* Footer */
.site-footer{position:absolute;top:2288px;left:0;width:1200px;height:416px;background:var(--footer);color:var(--footer-text)}
.footer-col{position:absolute;top:66px}
.footer-col h4{font-size:15px;font-weight:600;color:var(--white);margin-bottom:22px}
.footer-col p,.footer-col li{font-size:11px;line-height:22px}
.footer-about{left:110px;top:60px}
.social{display:flex;gap:8px;margin-bottom:22px}
.social span{width:30px;height:30px;border-radius:50%;border:2px solid var(--white);display:block}
.footer-contact{left:350px}
.footer-news{left:660px;width:200px}
.footer-news .field{height:30px;background:var(--white);margin-bottom:10px;font-size:10px;color:var(--gray);padding:8px 10px}
.footer-news .btn{padding:9px 16px;font-size:10px}
.footer-browse{left:960px}
.footer-browse ul{list-style:none}
.footer-browse li:before{content:"\203A";margin-right:6px;color:var(--white)}
.page-count{position:absolute;bottom:18px;right:40px;font-size:10px;color:var(--footer-text)}
</style>
</head>
<body>

<header class="site-header">
  <div class="brand"><span class="brand-mark"></span>Q7Systems</div>
  <nav class="main-nav">
    <a class="active" href="#">Home</a>
    <a href="#">About Us</a>
    <a href="#">Services</a>
    <a href="#">News</a>
    <a href="#">Projects</a>
    <a href="#">Contact Us</a>
    <svg width="12" height="12" viewBox="0 0 12 12"><circle cx="5" cy="5" r="3.6" fill="none" stroke="#555" stroke-width="1.5"/><line x1="7.6" y1="7.6" x2="11" y2="11" stroke="#555" stroke-width="1.5"/></svg>
  </nav>
</header>

<section class="hero" role="img" aria-label="Blue technology network background with glowing connected points">
  <svg class="hero-arrow prev" width="20" height="36" viewBox="0 0 20 36"><polyline points="16,2 4,18 16,34" fill="none" stroke="#fff" stroke-width="2"/></svg>
  <div class="hero-title">IT SERVICE EXCELLENCE</div>
  <div class="hero-sub">Striving for Continuous Service Improvement for our Clients</div>
  <a class="btn btn-orange" href="#">Get Started Now</a>
  <svg class="hero-arrow next" width="20" height="36" viewBox="0 0 20 36"><polyline points="4,2 16,18 4,34" fill="none" stroke="#fff" stroke-width="2"/></svg>
</section>

<section class="services">
  <h2 class="heading">What We Do</h2>
  <p class="lead">We deliver dependable <b>technology services</b> that keep your teams productive and your systems secure every single day.</p>
  <div class="service-grid">
    <div class="service">
      <svg width="40" height="40" viewBox="0 0 40 40" fill="none" stroke="#0255a3" stroke-width="2"><path d="M8 32 L24 16"/><circle cx="28" cy="12" r="6"/><path d="M6 8 L32 34"/></svg>
      <div><h3>IT Services</h3><p>Reliable planning and daily support that keeps every system running smoothly for your team.</p></div>
    </div>
    <div class="service">
      <svg width="40" height="40" viewBox="0 0 40 40" fill="none" stroke="#0255a3" stroke-width="2"><path d="M11 28 a7 7 0 0 1 1-14 a9 9 0 0 1 17 2 a6 6 0 0 1 0 12 Z"/></svg>
      <div><h3>Private Cloud</h3><p>Secure hosted platforms built around your data, with room to grow whenever you need it.</p></div>
    </div>
    <div class="service">
      <svg width="40" height="40" viewBox="0 0 40 40" fill="none" stroke="#0255a3" stroke-width="2"><rect x="10" y="18" width="20" height="16" rx="2"/><path d="M14 18 v-5 a6 6 0 0 1 12 0 v5"/></svg>
      <div><h3>Security Services</h3><p>Layered protection, monitoring and response that guard your network against modern threats.</p></div>
    </div>
    <div class="service">
      <svg width="40" height="40" viewBox="0 0 40 40" fill="none" stroke="#0255a3" stroke-width="2"><path d="M8 24 v-4 a12 12 0 0 1 24 0 v4"/><rect x="6" y="22" width="6" height="10" rx="2"/><rect x="28" y="22" width="6" height="10" rx="2"/></svg>
      <div><h3>Advanced Support</h3><p>Expert engineers ready to solve complex issues quickly and keep downtime to a minimum.</p></div>
    </div>
    <div class="service">
      <svg width="40" height="40" viewBox="0 0 40 40" fill="none" stroke="#0255a3" stroke-width="2"><rect x="6" y="8" width="28" height="20" rx="2"/><path d="M14 34 h12 M20 28 v6"/></svg>
      <div><h3>Fully Managed</h3><p>We take care of your complete environment so you can focus on running the business.</p></div>
    </div>
    <div class="service">
      <svg width="40" height="40" viewBox="0 0 40 40" fill="none" stroke="#0255a3" stroke-width="2"><circle cx="15" cy="16" r="6"/><circle cx="27" cy="26" r="6"/><path d="M15 6 v4 M15 22 v4 M5 16 h4 M21 16 h4"/></svg>
      <div><h3>Co-Managed IT</h3><p>Extra hands and tools that work alongside your in-house staff to share the load.</p></div>
    </div>
  </div>
</section>

<div class="divider"></div>

<section class="help">
  <h2 class="heading">How Can We Help Your Business?</h2>
  <p class="lead">Our team manages every layer of your setup to <b>provide complete technology management</b> solutions, giving you a clear path forward and the confidence to grow.</p>
  <div class="solution-row">
    <div class="solution"><div class="solution-photo photo-network" role="img" aria-label="Photo of network cables and a server rack"></div><h3>Your Network</h3><p>Fast, stable and secure connections across every office.</p></div>
    <div class="solution"><div class="solution-photo photo-web" role="img" aria-label="Photo of a website shown on several devices"></div><h3>Your Web Presence</h3><p>Sites and hosting that keep customers engaged online.</p></div>
    <div class="solution"><div class="solution-photo photo-apps" role="img" aria-label="Photo of hands using a tablet with application icons"></div><h3>Your Applications</h3><p>Business software deployed, updated and supported well.</p></div>
    <div class="solution"><div class="solution-photo photo-mind" role="img" aria-label="Photo of a relaxed person working at a laptop"></div><h3>Your Piece of Mind</h3><p>Proactive care so problems are solved before they start.</p></div>
  </div>
  <p class="partner-note">We proudly work with trusted partners to bring our clients proven tools and <b>leading solutions</b>.</p>
  <div class="partners">
    <span class="partner"><i class="round"></i>Sonora</span>
    <span class="partner"><i></i>Maxtrel</span>
    <span class="partner">Pictora</span>
    <span class="partner">Framestock</span>
    <span class="partner"><i></i>Quadrix</span>
  </div>
</section>

<section class="testimonials">
  <h2 class="heading">What Are People Saying About Q7Systems</h2>
  <div class="quote-row">
    <div class="quote"><p>“Their team responded within minutes and solved problems we had struggled with for months. Our office has never run so smoothly, and our staff finally trust their systems again.”</p><cite>Dana Morrow, City Name</cite></div>
    <div class="quote"><p>“Moving to their private cloud was painless. They planned every step, kept us informed the whole time, and our applications are now faster and far more secure than before.”</p><cite>Dana Morrow, City Name</cite></div>
    <div class="quote"><p>“We rely on their co-managed support to back up our own people. It feels like a true partnership, with clear reporting and honest advice whenever we need it most.”</p><cite>Dana Morrow, City Name</cite></div>
  </div>
</section>

<section class="difference">
  <h2 class="heading">We Are Different</h2>
  <p class="lead">We focus on long term relationships rather than quick fixes. Every client gets a dedicated team, clear pricing and regular reviews of their technology plan. Our engineers listen first, recommend only what adds real value, and stay with you from setup through daily support so your business can grow with complete confidence.</p>
  <a class="btn btn-blue" href="#">How It Works</a>
  <div class="difference-art" role="img" aria-label="Illustration of a friendly technician character"></div>
</section>

<footer class="site-footer">
  <div class="footer-col footer-about">
    <div class="social"><span></span><span></span><span></span></div>
    <p>©2024 Q7Systems Inc.<br>All Rights Reserved<br>Privacy Policy</p>
  </div>
  <div class="footer-col footer-contact">
    <h4>Contact us</h4>
    <p>1470 Harbor Point Drive, Suite 210<br>Fairview, CA 90210<br>1 (555) 014 2270<br>info@q7systems.com</p>
  </div>
  <div class="footer-col footer-news">
    <h4>Newsletter</h4>
    <div class="field">Name</div>
    <div class="field">Email Address</div>
    <a class="btn btn-blue" href="#">Submit</a>
  </div>
  <div class="footer-col footer-browse">
    <h4>Browse</h4>
    <ul>
      <li>Managed Services</li>
      <li>Private Cloud</li>
      <li>Security Solutions</li>
      <li>Advanced Support</li>
      <li>Client Resources</li>
    </ul>
  </div>
  <div class="page-count">1/4</div>
</footer>

</body>
</html>
```